International freight forwarder experienced in perishable handling needs a web design

We need a website designed that will allow us to capture more customers through the website. We would like a visually appealing design that is not so heavy on text. Our business covers the logistics and freight forwarding industries and we have offices in South America and the USA. Our main customers are importers USA, Europe, Asia and Russia and we currently work almost exclusively with perishable products such as fresh cut flowers, fresh exotics fruits, cacao, fresh fish etc. We would like to convey a fresh, modern approach to freight forwarding focusing on concepts such as - time sensitive, anytime-anywhere delivery, innovation, experience, reliability and confidence. Should include links with Plumetta and Worvanet. Our core solutions include: Core Services
*Air Freight
*Ocean Freight
*Warehousing & Distribution
Our industry solutions cover
*Flowers
*FMCG including, fruits, vegetables
*Live animals
*Automotive
*Consumer Goods
*Industrial
*Oil & Gas
*Pharma
* Event logistics
* Project logistics

Target Market(s)

Importers in Europe, USA, Asia, Middle East and Russia

Number of Pages Required

4 page

Font styles to use
Sans Serif

Colors
a1cd39
606060
000000

Requirements
Must have
• Photos of fresh cut flowers, FMCG such as cacao, fresh fish (packaged for shipping), fresh exotic fruits, pharma products (packaged for shipping), oil and gas etc. Internal customer login access
Nice to have
• Photos of cargo shipping carriers and cargo airline carriers. Features similar to those of following website http://www.brolvacargo.com/eng/main/index.jsp?FromURL=web
Should not have
• Too much text, needs to be visually pleasing

```html
<!DOCTYPE html>
<html lang="en">
<head>
<meta charset="utf-8">
<title>Corvane Alliance Group – Freight Forwarding</title>
<link href="https://fonts.googleapis.com/css2?family=Lato:ital,wght@0,400;0,700;1,400&family=Oswald:wght@400&display=swap" rel="stylesheet">
<style>
:root{
  --green:#a1cd39;
  --grey:#606060;
  --black:#000;
  --panel:#2e2e2e;
  --dark:#242424;
  --field:#c9c9c9;
  --white:#fff;
}
*{box-sizing:border-box;margin:0;padding:0}
html,body{width:1097px;height:1200px;overflow:hidden;background:#1f1f1f;font-family:"Lato",sans-serif}
.page{position:relative;width:1097px;height:1200px;overflow:hidden}
.abs{position:absolute}

/* header */
.site-header{position:absolute;left:0;top:0;width:1097px;height:97px;background:var(--white)}
.brand{position:absolute;left:120px;top:0;width:223px;height:130px;background:var(--white);border-radius:0 0 8px 8px;box-shadow:0 3px 6px rgba(0,0,0,.35);z-index:3;text-align:center}
.brand-mark{width:48px;height:48px;border-radius:50%;background:var(--green);margin:12px auto 0}
.brand-name{font-size:27px;color:var(--grey);margin-top:16px;letter-spacing:-.3px}
.phone{position:absolute;left:843px;top:18px;display:flex;align-items:center;gap:8px;font-weight:700;font-size:16px;color:#111}
.main-nav{position:absolute;top:69px;left:0;width:1097px;font-size:14px;color:var(--grey);font-weight:700}
.main-nav a{position:absolute;color:var(--grey);text-decoration:none;letter-spacing:.2px}
.main-nav a.active{color:var(--green);border-bottom:2px solid var(--green);padding-bottom:1px}

/* hero */
.hero{position:absolute;left:0;top:97px;width:1097px;height:410px;background:radial-gradient(ellipse at 55% 45%,#b24f78 0%,#8a5a4e 30%,#6f6457 55%,#3d3a36 100%)}
.hero-caption{position:absolute;left:120px;top:267px;width:355px;height:88px;background:rgba(30,30,30,.85);border-left:6px solid var(--green);padding:10px 0 0 16px;font-family:"Oswald",sans-serif;font-size:27px;line-height:34px;color:var(--white)}
.dots{position:absolute;top:446px;left:507px;display:flex;gap:7px}
.dots span{width:15px;height:15px;border-radius:50%;background:var(--white)}
.dots span.on{background:var(--green);box-shadow:inset 0 0 0 3px var(--white)}

/* body band */
.body-band{position:absolute;left:0;top:507px;width:1097px;height:440px;background:#262626}
.services{position:absolute;left:128px;top:486px;width:840px;height:102px;display:flex;border-radius:4px;overflow:hidden;z-index:2}
.service{flex:1;background:var(--black);color:var(--white);text-align:center;font-size:17px;padding-top:24px}
.service svg{display:block;margin:0 auto 10px}
.service.active{background:var(--green);border-top:9px solid #5c5c5c;padding-top:15px}
.service b{font-weight:700}

.panel{position:absolute;top:627px;width:279px;height:285px;background:var(--panel);border:1px solid #4a4a4a;border-radius:4px;overflow:hidden}
.panel-head{position:absolute;left:0;top:0;width:279px;height:62px}
.panel-icon{position:absolute;left:18px;top:3px;width:40px;height:40px;border-radius:50%;background:var(--white);border:3px solid #ddd}
.panel-title{position:absolute;left:70px;top:10px;font-size:17px;color:#111}
.panel-title b{font-weight:700}
.about-text{position:absolute;left:13px;top:64px;width:256px;font-size:12.4px;line-height:16.8px;color:#e6e6e6;letter-spacing:.55px}
.more{position:absolute;left:8px;width:98px;height:22px;background:var(--black);color:var(--white);font-size:12px;font-weight:700;padding:4px 0 0 9px;clip-path:polygon(0 0,100% 0,88% 100%,0 100%)}
.news-item{position:absolute;left:16px;width:250px}
.date{position:absolute;left:0;top:0;width:43px;height:44px;text-align:center;border-radius:3px;overflow:hidden}
.date .d{background:var(--black);color:var(--white);font-size:18px;height:27px;padding-top:3px}
.date .m{background:#5a5a5a;color:#ddd;font-size:11px;font-weight:700;height:17px;padding-top:2px}
.news-item h3{position:absolute;left:60px;top:0;font-size:13.5px;color:var(--white);font-weight:700;white-space:nowrap}
.news-item p{position:absolute;left:60px;top:22px;width:195px;font-size:11px;line-height:16.5px;color:#ddd}
.divider{position:absolute;left:16px;top:140px;width:248px;border-top:1px dashed #555}
.field{position:absolute;left:17px;width:246px;height:28px;background:var(--field);border-radius:3px;border:1px solid #e0e0e0;font-size:11px;font-style:italic;color:#444;padding:8px 0 0 15px}

/* industries */
.industry{position:absolute;left:0;top:947px;width:1097px;height:68px;background:#060606}
.industry-title{position:absolute;left:121px;top:10px;font-size:16.5px;font-weight:700;color:var(--green);line-height:22px}
.industry-list{position:absolute;left:320px;font-size:13.5px;color:var(--white)}
.industry-list span{position:absolute;white-space:nowrap}
.industry-list span::before{content:"• ";color:var(--green)}
.strip{position:absolute;left:0;top:1015px;width:1097px;height:30px;background:#2b2b2b}

/* newsletter */
.newsletter{position:absolute;left:0;top:1045px;width:1097px;height:42px;background:linear-gradient(#5a5a5a,#3c3c3c)}
.newsletter .label{position:absolute;left:120px;top:9px;font-size:17px;color:var(--white)}
.email-box{position:absolute;left:320px;top:8px;width:191px;height:25px;background:#1a1a1a;border:1px solid #111;border-radius:2px;font-size:11px;font-style:italic;color:#ccc;padding:6px 0 0 8px}
.subscribe{position:absolute;left:519px;top:8px;width:78px;height:25px;background:var(--green);border-radius:2px;font-size:12px;font-weight:700;color:#111;text-align:center;padding-top:5px}
.follow{position:absolute;left:760px;top:10px;font-size:17px;color:var(--white)}
.social{position:absolute;top:7px;width:27px;height:27px;border-radius:50%;background:#5d7fa8}

/* footer */
.site-footer{position:absolute;left:0;top:1087px;width:1097px;height:113px;background:#222}
.foot-nav{position:absolute;left:0;top:19px;width:1097px;text-align:center;font-size:11px;color:#ddd}
.foot-nav i{font-style:normal;margin:0 7px}
.contact{position:absolute;top:50px;font-size:12.5px;color:#e6e6e6;display:flex;align-items:center;gap:8px;white-space:nowrap}
.copy{position:absolute;left:0;top:85px;width:1097px;text-align:center;font-size:11px;color:#ddd}
</style>
</head>
<body>
<div class="page">

  <header class="site-header">
    <div class="phone">
      <svg width="24" height="24" viewBox="0 0 24 24"><circle cx="12" cy="12" r="11" fill="none" stroke="#a1cd39" stroke-width="2"/><path d="M8 6c1 0 2 2 2 3s-1 1-1 2 2 3 3 3 1-1 2-1 3 1 3 2-1 2-2 2c-4 0-9-5-9-9 0-1 1-2 2-2z" fill="#a1cd39"/></svg>
      555 014 2290
    </div>
    <nav class="main-nav">
      <a class="active" style="left:421px">HOME</a>
      <a style="left:492px">ABOUT US</a>
      <a style="left:591px">SERVICES</a>
      <a style="left:685px">OUR NETWORK</a>
      <a style="left:819px">NEWS</a>
      <a style="left:889px">CONTACT US</a>
    </nav>
  </header>
  <div class="brand">
    <div class="brand-mark"></div>
    <div class="brand-name">Corvane Alliance</div>
  </div>

  <section class="hero" role="img" aria-label="Worker loading a netted pallet of boxed fresh-cut flowers inside a cargo aircraft hold">
    <div class="hero-caption">Most Extensive Hub Operations<br>In The ASEAN Region</div>
    <div class="dots"><span></span><span class="on"></span><span></span><span></span></div>
  </section>

  <div class="body-band"></div>

  <div class="services">
    <div class="service">
      <svg width="52" height="20" viewBox="0 0 52 20"><path d="M2 12 L40 4 Q50 2 50 6 Q50 9 42 11 L12 17 Z M18 10 L26 1 L31 1 L27 8 Z M10 13 L4 6 L8 6 L14 11 Z" fill="#fff"/></svg>
      <b>Air</b> Freight
    </div>
    <div class="service active">
      <svg width="52" height="26" viewBox="0 0 52 26"><path d="M2 16 H50 L44 24 H8 Z M12 15 V9 H36 V15 Z M18 9 V4 H28 V9 Z M30 4 h4 v5 h-4z" fill="#fff"/></svg>
      <b>Ocean</b> Freight
    </div>
    <div class="service">
      <svg width="40" height="28" viewBox="0 0 40 28"><path d="M2 10 L20 2 L38 10 V13 H2 Z M4 14 H36 V27 H30 V17 H10 V27 H4 Z M11 18 H29 V20 H11 Z M11 22 H29 V24 H11 Z" fill="#fff"/></svg>
      <b>Warehousing</b> &amp; Distribution
    </div>
  </div>

  <!-- About panel -->
  <article class="panel" style="left:122px">
    <svg class="panel-head" viewBox="0 0 279 62"><path d="M0 0H279V60Q140 40 0 62Z" fill="#a1cd39"/></svg>
    <div class="panel-icon"></div>
    <h2 class="panel-title" style="font-weight:400">About <b>Corvane</b> Alliance</h2>
    <p class="about-text">Lorem ipsum dolor sit amet, consectet adipiscing elit. Praesent vestibulum molestie lacus. Aenean nonummy hendrerit mauris. Phasellus por. Lorem ipsum dolor sit amet, consectetuer adipisci elit. Praesent vestibulum molestie lacus. An nonummy hendrerit mauris. Phasellus porta. Lorem ipsum dolor sit amet, consectetuer adipiscing Praesent vestibulum molestie lacus. Aenean non hendrerit mauris. Phasellus porta.Lorem ipsum</p>
    <div class="more" style="top:247px">Read more »</div>
  </article>

  <!-- News panel -->
  <article class="panel" style="left:409px">
    <svg class="panel-head" viewBox="0 0 279 62"><path d="M0 0H279V60Q140 40 0 62Z" fill="#a1cd39"/></svg>
    <div class="panel-icon"></div>
    <h2 class="panel-title"><b>Our News</b></h2>
    <div class="news-item" style="top:67px">
      <div class="date"><div class="d">01</div><div class="m">APR</div></div>
      <h3>Lorem Ipsum Dolor Sit Ametc</h3>
      <p>Lorem ipsum dolor sit amet, consectet uer adimpisciged diamr nonummy</p>
    </div>
    <div class="divider"></div>
    <div class="news-item" style="top:158px">
      <div class="date"><div class="d">02</div><div class="m">APR</div></div>
      <h3>Biam nonummy nibh euismod</h3>
      <p>Lorem ipsum dolor sit amet, consectet adimpisciged diamr nonummy nibh euismod tincidunt ut</p>
    </div>
    <div class="more" style="top:246px">Read more »</div>
  </article>

  <!-- Inquiry panel -->
  <article class="panel" style="left:696px">
    <svg class="panel-head" viewBox="0 0 279 62"><path d="M0 0H279V60Q140 40 0 62Z" fill="#a1cd39"/></svg>
    <div class="panel-icon"></div>
    <h2 class="panel-title"><b>Quick</b> Inquiry</h2>
    <div class="field" style="top:66px">Full Name</div>
    <div class="field" style="top:104px">Email Address</div>
    <div class="field" style="top:142px">Phone&nbsp; Number</div>
    <div class="field" style="top:180px;height:53px">Message</div>
    <div class="more" style="top:245px;width:96px">Submit »</div>
  </article>

  <section class="industry">
    <div class="industry-title">Our Industry<br>Solutions Cover</div>
    <svg class="abs" style="left:256px;top:0" width="30" height="68" viewBox="0 0 30 68"><path d="M0 0 L28 34 L0 68 Z" fill="#1e1e1e"/></svg>
    <div class="industry-list" style="top:12px">
      <span style="left:0">Flowers</span>
      <span style="left:82px">FMCG including, fruits, vegetables</span>
      <span style="left:328px">Live animals</span>
      <span style="left:431px">Automotive</span>
      <span style="left:537px">Consumer Goods</span>
    </div>
    <div class="industry-list" style="top:39px">
      <span style="left:0">Industrial</span>
      <span style="left:94px">Oil &amp; Gas</span>
      <span style="left:189px">Pharma</span>
      <span style="left:272px">Event logistics</span>
      <span style="left:394px">Project logistics</span>
    </div>
  </section>
  <div class="strip"></div>

  <section class="newsletter">
    <div class="label">Subscribe to newsletter</div>
    <div class="email-box">Enter Email Here</div>
    <div class="subscribe">Subscribe</div>
    <div class="follow">Follow us</div>
    <span class="social" style="left:838px;background:#4a6fa0" role="img" aria-label="Plumetta"></span>
    <span class="social" style="left:875px;background:#3ba7d6" role="img" aria-label="Chirrly"></span>
    <span class="social" style="left:912px;background:#2f7fae" role="img" aria-label="Worvanet"></span>
    <span class="social" style="left:949px;background:#c8463a" role="img" aria-label="Glimora"></span>
  </section>

  <footer class="site-footer">
    <nav class="foot-nav">Home<i>|</i>About Us<i>|</i>Services<i>|</i>Our Network<i>|</i>News<i>|</i>Contact Us</nav>
    <div class="contact" style="left:192px">
      <svg width="12" height="16" viewBox="0 0 12 16"><path d="M6 0a6 6 0 0 1 6 6c0 4-6 10-6 10S0 10 0 6a6 6 0 0 1 6-6z" fill="#a1cd39"/><circle cx="6" cy="6" r="2.2" fill="#222"/></svg>
      8/F Harrow Freight Centre, 21 Tidewell Road, Port Selby
    </div>
    <div class="contact" style="left:600px">
      <svg width="13" height="13" viewBox="0 0 24 24"><path d="M5 2c2 0 3 4 3 5s-2 2-2 3 4 7 6 7 2-2 3-2 5 1 5 3-2 4-3 4C10 22 2 14 2 5c0-1 1-3 3-3z" fill="#a1cd39"/></svg>
      555 014 2290
    </div>
    <div class="contact" style="left:714px">
      <svg width="14" height="10" viewBox="0 0 14 10"><rect width="14" height="10" fill="#a1cd39"/><path d="M0 0 L7 6 L14 0" fill="none" stroke="#222" stroke-width="1.5"/></svg>
      info@corvanealliancegroup.com
    </div>
    <div class="copy">© 2015 CorvaneAllianceGroup, All Right Reserved</div>
  </footer>

</div>
</body>
</html>
```